Design a Mother's Day Flyer

Mothers Day
Sunday 14th May 2017

Special Mothers Day Menu for Lunch & Dinner
Regular Al a Carte Dining for Breakfast

Adults 2 Course $55 & 3 Course $65
Children 1 Course $13 & 2 Course $18

Entree
Twice Cooked Pork Belly with apple and radish salad
or
Roast chicken, speck bacon, fire roasted red pepper and Israeli couscous salad

Main
Braised beef cheeks with sweet potato puree and roasted carrots
or
Slow cooked salmon with broccoli and hazelnut salad
or
Spinach and ricotta cannelloni topped with a rocket, Parmesan and walnut salad

Dessert
Lemon Cheesecake with summer berry and mint salad
or
Milk chocolate and hazelnut cake served with cream & seasonal berries

Book with us and go in the draw to win a $200 voucher for Marlo T Health & Beauty Spa

Call us on 6417 9082 or email bookings@fernwickdining.example for more information

```html
<!DOCTYPE html>
<html lang="en">
<head>
<meta charset="utf-8">
<title>Fernwick Mothers Day Flyer</title>
<link rel="stylesheet" href="https://fonts.googleapis.com/css2?family=Great+Vibes&family=Montserrat:wght@500;600&family=Open+Sans:wght@600&family=Oswald:wght@600;700&display=swap">
<style>
  :root {
    --rose: #e0627a;
    --rose-deep: #d9566f;
    --cream: #f7e6d3;
    --cream-soft: #f3dcc6;
    --teal: #6db7b2;
    --ink: #2a2526;
    --white: #ffffff;
    --stage: #ececec;
  }
  * { margin: 0; padding: 0; box-sizing: border-box; }
  html, body { width: 1090px; height: 1200px; overflow: hidden; }
  body { background: var(--stage); position: relative; }

  .flyer {
    position: absolute; left: 102px; top: 26px;
    width: 885px; height: 1148px; overflow: hidden;
    background: linear-gradient(180deg, var(--cream) 0%, var(--cream-soft) 100%);
    font-family: "Open Sans", sans-serif; color: var(--ink);
  }
  .flyer-shapes { position: absolute; inset: 0; }

  .brand { position: absolute; left: 48px; top: 40px; width: 225px; text-align: left; }
  .brand-name { font-family: "Montserrat", sans-serif; font-weight: 500; font-size: 58px; line-height: 1; color: var(--ink); }
  .brand-tag { font-family: "Montserrat", sans-serif; font-weight: 500; font-size: 21px; letter-spacing: 0.5px; margin-top: 92px; color: var(--ink); }

  .event-badge { position: absolute; left: 412px; top: 5px; width: 470px; height: 335px; }

  .headline {
    position: absolute; left: 0; right: 0; top: 378px; text-align: center;
    font-family: "Oswald", sans-serif; font-weight: 700; font-size: 34px; line-height: 45px;
  }
  .accent { color: var(--rose); }

  .pricing {
    position: absolute; left: 0; right: 0; top: 548px; text-align: center;
    font-family: "Oswald", sans-serif; font-weight: 600; font-size: 25px; line-height: 32px;
  }

  .menu { position: absolute; top: 640px; left: 92px; width: 700px; display: flex; justify-content: space-between; }
  .course { width: 200px; text-align: center; font-size: 13.5px; line-height: 19px; }
  .course h2 { font-family: "Montserrat", sans-serif; font-weight: 600; font-size: 20px; color: var(--rose); margin-bottom: 6px; }
  .course .or { margin: 4px 0; }

  .prize-draw {
    position: absolute; left: 0; right: 0; top: 885px; text-align: center;
    font-family: "Oswald", sans-serif; font-weight: 600; font-size: 26px; line-height: 34px;
  }
  .prize-draw .amount { font-size: 31px; }

  .event-date {
    position: absolute; left: 0; top: 990px; width: 200px; text-align: center;
    font-family: "Montserrat", sans-serif; font-weight: 600; font-size: 33px; line-height: 50px; color: var(--white);
  }

  .contact { position: absolute; left: 460px; width: 420px; top: 1020px; text-align: center; font-family: "Oswald", sans-serif; font-weight: 600; }
  .contact-label { font-size: 25px; line-height: 34px; }
  .contact-phone { font-size: 45px; line-height: 54px; }
  .contact-email { font-size: 19px; line-height: 28px; }
</style>
</head>
<body>
  <main class="flyer">
    <svg class="flyer-shapes" width="885" height="1148" viewBox="0 0 885 1148" aria-hidden="true">
      <polygon points="0,0 885,0 885,60 480,248 0,322" fill="var(--rose)"/>
      <polygon points="0,330 505,253 0,350" fill="var(--rose)"/>
      <polygon points="0,362 445,275 0,376" fill="var(--teal)"/>
      <polygon points="0,892 0,1148 438,1148" fill="var(--rose)"/>
      <polygon points="300,1062 560,1016 305,1070" fill="var(--rose)"/>
      <polygon points="430,1148 885,1148 885,1000 720,985 545,1035" fill="var(--white)"/>
      <polygon points="730,1000 885,1080 885,1088" fill="var(--cream-soft)"/>
    </svg>

    <div class="brand">
      <div class="brand-name">Fernwick</div>
      <div class="brand-tag">RESTAURANT &amp; BAR</div>
    </div>

    <svg class="event-badge" viewBox="0 0 470 335" aria-label="Mothers Day">
      <path d="M70,15 H400 Q400,62 455,62 V273 Q400,273 400,320 H70 Q70,273 15,273 V62 Q70,62 70,15 Z" fill="var(--teal)"/>
      <path d="M80,28 H390 Q392,72 442,74 V261 Q392,263 390,307 H80 Q78,263 28,261 V74 Q78,72 80,28 Z" fill="var(--cream)"/>
      <path d="M90,40 H380 Q383,82 430,86 V249 Q383,253 380,295 H90 Q87,253 40,249 V86 Q87,82 90,40 Z" fill="var(--rose)"/>
      <text x="235" y="150" text-anchor="middle" font-family="'Great Vibes', cursive" font-size="72" fill="var(--ink)">Mothers</text>
      <text x="250" y="245" text-anchor="middle" font-family="'Great Vibes', cursive" font-size="72" fill="var(--ink)">Day</text>
    </svg>

    <h1 class="headline">Special Mothers Day Menu for<br>Lunch &amp; <span class="accent">Dinner Regular</span> Al a Carte<br>Dining for Breakfast</h1>

    <div class="pricing">
      <p>Adults 2 Course......<span class="accent">$55</span> &amp; 3 Course......<span class="accent">$65</span></p>
      <p>Children 1 Course.. <span class="accent">$13</span> &amp; 2 Course......<span class="accent">$18</span></p>
    </div>

    <section class="menu">
      <div class="course">
        <h2>Entree</h2>
        <p>Twice Cooked Pork Belly with apple and radish salad</p>
        <p class="or">or</p>
        <p>Roast chicken, speck bacon, fire roasted red pepper and Israeli cous-cous salad</p>
      </div>
      <div class="course">
        <h2>Main</h2>
        <p>Braised beef cheeks with sweet potato puree and roasted carrots</p>
        <p>or</p>
        <p>Slow cooked salmon with broccoli and hazelnut salad</p>
        <p>or</p>
        <p>Spinach and ricotta cannelloni topped with a rocket, Parmesan and walnut salad</p>
      </div>
      <div class="course">
        <h2>Dessert</h2>
        <p>Lemon Cheesecake with summer berry and mint salad</p>
        <p class="or">or</p>
        <p>Milk chocolate and hazelnut cake served with cream &amp; seasonal berries</p>
      </div>
    </section>

    <p class="prize-draw">Book with us and go in the draw to win a <span class="accent amount">$200</span><br>voucher for Marlo T <span class="accent">Health &amp; Beauty</span> Spa</p>

    <p class="event-date">Sunday<br>14th May<br>2017</p>

    <div class="contact">
      <p class="contact-label">Call us on</p>
      <p class="contact-phone">6417 9082</p>
      <p class="contact-email">email bookings<span class="accent">@fernwickdining.example</span></p>
    </div>
  </main>
</body>
</html>
```